'SOLVANO' NEW WINE LABEL DESIGN

I am looking for an exceptional and exciting design for a wine label called 'Solvano' meaning 'Lookout'. The design must feature the name 'Solvano', and the word 'Cabernet Sauvignon' in version 1 and 'Sauvignon Blanc' in version 2. It will also need the words 'Valle Central, Chile' at the bottom of the label as a prominent piece of information as well as the vintage 2017. Please produce the work in size 80mm x 100mm. Feel free to use colour in addition to black/white and ensue that the label is easy to read on a shelf placement.
Low design quality
Target Market(s)
SUPERMARKETS & WINE STORES
Requirements
Must have
- EASY TO READ, USE COLOURS LIKE GREEN FOR SAUVIGNON & RED FOR CABERNET SAUVIGNON
- FULL BOTTLE SHOT MUST BE IN PROVIDED DESIGNS. ALL BOTTLE TOPS SHOULD BE VENDRAX STYLE (SCREW TOP)
- PLEASE NOTE THAT LABEL INFORMATION MUSY BE EASY TO READ I.E. VINTAGE, PLACE OF ORGIN ALTHOUGH NOT THE MAIN CONTENT MUST STILL BE CLEAR.
Nice to have
- ARTISTIC REFERENCE LINK TO NAME & ANDES BUT NOT PICTURES OF MOUNTAINS
Should not have
- PICTURES OF GRAPES
- PICTURES OF VINEYARDS
- PICTURES OF MOUNTAINS

```html
<!DOCTYPE html>
<html lang="en">
<head>
<meta charset="utf-8">
<title>Solvano – Wine Labels</title>
<link href="https://fonts.googleapis.com/css2?family=Josefin+Sans:wght@400;600&family=Roboto+Slab:wght@700&display=swap" rel="stylesheet">
<style>
  :root {
    --page: #ffffff;
    --stage: #c7cfce;
    --label: #f1f2ee;
    --ink: #111111;
    --muted: #4a4a4a;
    --cabernet: #9e1b1f;
    --cabernet-soft: rgba(158, 27, 31, 0.28);
    --blanc: #7cc617;
    --blanc-soft: rgba(124, 198, 23, 0.32);
  }
  * { box-sizing: border-box; margin: 0; padding: 0; }
  html, body { width: 1200px; height: 1000px; overflow: hidden; background: var(--page); }
  .canvas { position: relative; width: 1200px; height: 1000px; overflow: hidden; }
  .stage {
    position: absolute; left: 0; top: 0; width: 672px; height: 1000px;
    background: var(--stage);
  }
  .label {
    position: absolute; top: 440px; width: 250px; height: 312px;
    background: var(--label);
    overflow: hidden;
    box-shadow: 0 2px 6px rgba(0,0,0,0.12);
  }
  .label--cabernet { left: 70px; --accent: var(--cabernet); --accent-soft: var(--cabernet-soft); }
  .label--blanc { left: 352px; --accent: var(--blanc); --accent-soft: var(--blanc-soft); }
  .label__art {
    position: absolute; left: 0; top: 0; width: 58%; height: 100%;
    background: linear-gradient(160deg, var(--accent-soft) 0%, rgba(255,255,255,0) 85%);
  }
  .label__name {
    position: absolute; left: 0; right: 0; top: 68px;
    text-align: center;
    font-family: "Josefin Sans", sans-serif; font-weight: 400;
    font-size: 30px; letter-spacing: 0.5px; color: var(--ink);
    padding-left: 28px;
  }
  .label__variety {
    position: absolute; right: 16px; top: 170px;
    text-align: right;
    font-family: "Josefin Sans", sans-serif; font-weight: 400;
    font-size: 15px; line-height: 1.1; color: var(--muted);
  }
  .label__origin {
    position: absolute; right: 16px; top: 228px;
    text-align: right;
    font-family: "Roboto Slab", serif; font-weight: 700;
    font-size: 10px; line-height: 1.3; color: var(--muted);
  }
  .label__vintage {
    position: absolute; right: 16px; top: 262px;
    font-family: "Josefin Sans", sans-serif; font-weight: 600;
    font-size: 7px; letter-spacing: 0.5px; color: var(--muted);
  }
  .wordmark {
    position: absolute; left: 742px;
    display: flex; align-items: center; gap: 12px;
    font-family: "Josefin Sans", sans-serif; font-weight: 400;
    font-size: 76px; line-height: 1; letter-spacing: 0; color: var(--ink);
    white-space: nowrap;
  }
  .wordmark--cabernet { top: 314px; }
  .wordmark--blanc { top: 622px; }
  .wordmark__swatch { flex: 0 0 14px; width: 14px; height: 14px; }
  .wordmark--cabernet .wordmark__swatch { background: var(--cabernet); }
  .wordmark--blanc .wordmark__swatch { background: var(--blanc); }
</style>
</head>
<body>
<main class="canvas">
  <section class="stage">
    <article class="label label--cabernet">
      <div class="label__art" role="img" aria-label="Fine red line drawing of branching ridges running down the left side of the label"></div>
      <h2 class="label__name">SOLVANO</h2>
      <p class="label__variety">CABERNET<br>SAUVIGNON</p>
      <p class="label__origin">Valle Central<br>CHILE</p>
      <p class="label__vintage">VINTAGE 2017</p>
    </article>
    <article class="label label--blanc">
      <div class="label__art" role="img" aria-label="Fine green line drawing of branching ridges running down the left side of the label"></div>
      <h2 class="label__name">SOLVANO</h2>
      <p class="label__variety">SAUVIGNON<br>BLANC</p>
      <p class="label__origin">Valle Central<br>CHILE</p>
      <p class="label__vintage">VINTAGE 2017</p>
    </article>
  </section>
  <div class="wordmark wordmark--cabernet"><span>SOLVANO</span><span class="wordmark__swatch"></span></div>
  <div class="wordmark wordmark--blanc"><span>SOLVANO</span><span class="wordmark__swatch"></span></div>
</main>
</body>
</html>
```